Brisk Meadow Builders needs an updated flyer

Instructions are in a .pdf called "Instructions. All photos and logos are included along with the original flyer in .ai

We are looking for a fresh design that promotes sustainability.

```html
<!DOCTYPE html>
<html lang="en">
<head>
<meta charset="utf-8">
<title>Brisk Meadow Builders – Mobile Vending Flyer</title>
<link href="https://fonts.googleapis.com/css2?family=Roboto+Condensed:wght@400;500;700&family=Roboto:wght@400;500;700&display=swap" rel="stylesheet">
<style>
  :root{
    --green-dark:#2d6b22;
    --green:#3c8a2c;
    --green-light:#8cc76a;
    --yellow:#f5a70f;
    --white:#ffffff;
    --ink:#1d1d1d;
    --backdrop:#e9eaec;
  }
  *{box-sizing:border-box;margin:0;padding:0}
  html,body{width:720px;height:1200px;overflow:hidden;background:var(--backdrop)}
  body{font-family:"Roboto",Arial,sans-serif;color:var(--ink)}
  .flyer{position:absolute;left:15px;top:112px;width:690px;height:976px;background:var(--white);overflow:hidden;box-shadow:0 6px 22px rgba(0,0,0,.18)}
  .hero-photo{position:absolute;left:0;top:0;width:690px;height:445px;
    background:linear-gradient(180deg,#6d8fb4 0%,#a8bccf 22%,#5f7a55 45%,#3f5d33 70%,#4a6a3a 100%)}
  .hero-house{position:absolute;left:340px;top:40px;width:310px;height:370px;
    background:linear-gradient(180deg,#e9ecec 0%,#f4f4f2 60%,#c9b58e 100%);border-radius:4px;opacity:.92}
  .shapes{position:absolute;left:0;top:0}
  .brand{position:absolute;left:30px;top:110px;width:230px;display:flex;align-items:center;gap:8px}
  .brand-dot{width:14px;height:14px;border-radius:50%;background:var(--green);flex:none}
  .brand-name{font-family:"Roboto Condensed",Arial,sans-serif;font-weight:700;font-size:23px;line-height:1.05;color:var(--green);text-transform:uppercase}
  .tagline{position:absolute;left:22px;top:212px;width:320px;font-family:"Roboto Condensed",Arial,sans-serif;font-weight:700;font-size:26.5px;line-height:32px;color:var(--white);text-transform:uppercase;padding-left:22px}
  .tagline .q{position:absolute;font-size:34px;line-height:1}
  .tagline .q-open{left:0;top:-6px}
  .tagline .q-close{font-size:34px;position:relative;top:12px;margin-left:6px}
  .price-badge{position:absolute;left:503px;top:306px;width:186px;height:186px;border-radius:50%;background:var(--green-dark);border:4px solid var(--white);
    display:flex;flex-direction:column;align-items:center;justify-content:center;font-family:"Roboto Condensed",Arial,sans-serif;font-weight:700;color:var(--white);text-transform:uppercase;text-align:center;line-height:1}
  .price-badge .small{font-size:19px}
  .price-badge .big{font-size:32px;margin:3px 0}
  .price-badge .price{font-size:34px;color:var(--yellow);margin-top:8px}
  .features-title{position:absolute;left:39px;top:442px;width:252px;height:40px;background:var(--green-light);border-radius:0 20px 20px 0;
    font-family:"Roboto Condensed",Arial,sans-serif;font-weight:700;font-size:22px;color:var(--ink);display:flex;align-items:center;padding-left:13px;text-transform:uppercase}
  .feature-list{position:absolute;list-style:none;color:var(--white);font-size:11.5px;line-height:14px}
  .feature-list li{position:relative;padding-left:24px;margin-bottom:8px}
  .feature-list.right li{margin-bottom:6px}
  .feature-list svg{position:absolute;left:0;top:1px;width:11px;height:11px}
  .feature-list.left{left:42px;top:497px;width:240px}
  .feature-list.right{left:374px;top:493px;width:300px}
  .divider-v{position:absolute;left:334px;top:497px;width:2px;height:120px;background:var(--ink)}
  .unit-photo{position:absolute;border-radius:3px;background:linear-gradient(180deg,#cfd6d9 0%,#f2f2f0 45%,#dadada 80%,#b99d6f 100%)}
  .unit-photo.one{left:36px;top:622px;width:218px;height:135px}
  .unit-photo.two{left:283px;top:624px;width:140px;height:150px}
  .unit-photo.three{left:465px;top:620px;width:190px;height:132px}
  .block-title{font-family:"Roboto Condensed",Arial,sans-serif;font-weight:700;font-size:23px;line-height:24px;color:var(--green)}
  .options{position:absolute;left:42px;top:772px;width:290px}
  .options ul{list-style:none;margin-top:6px;font-size:12.2px;line-height:16px;color:var(--ink)}
  .options li{position:relative;padding-left:23px}
  .options li::before{content:"";position:absolute;left:2px;top:5px;width:6px;height:6px;border-radius:50%;background:var(--green)}
  .options .note{margin-top:8px;font-family:"Roboto Condensed",Arial,sans-serif;font-weight:500;font-size:15.5px;line-height:18px;color:var(--ink)}
  .divider-col{position:absolute;left:348px;top:784px;width:1px;height:130px;border-left:1px dashed #9a9a9a}
  .use-cases{position:absolute;left:377px;top:772px;width:295px}
  .use-cases p{font-size:11px;line-height:13px;color:var(--ink);margin-top:6px}
  .use-cases .label{color:var(--green)}
  .use-cases .cta{font-family:"Roboto Condensed",Arial,sans-serif;font-weight:700;font-size:15.5px;line-height:17px;margin-top:8px}
  .footer{position:absolute;left:0;top:935px;width:690px;height:41px;background:var(--yellow);display:flex;align-items:center;justify-content:center;gap:22px;font-size:14.5px;color:var(--ink)}
  .footer span{display:flex;align-items:center;gap:6px}
  .footer svg{width:14px;height:14px}
</style>
</head>
<body>
<svg width="0" height="0" style="position:absolute">
  <symbol id="tick" viewBox="0 0 12 12"><circle cx="6" cy="6" r="5.2" fill="none" stroke="#ffffff" stroke-width="1"/><path d="M3.6 6.2 5.3 7.8 8.5 4.4" fill="none" stroke="#ffffff" stroke-width="1.2"/></symbol>
</svg>

<main class="flyer">
  <div class="hero-photo" role="img" aria-label="Photo of a white farmhouse-style tiny vending house with solar roof and wooden porch deck, trees and sky behind"></div>
  <div class="hero-house" role="img" aria-label="Tiny farmhouse vending unit with open door and fold-down deck"></div>

  <svg class="shapes" width="690" height="700" viewBox="0 0 690 700">
    <defs>
      <linearGradient id="tint" x1="0" y1="0" x2="1" y2="0">
        <stop offset="0" stop-color="#1f4a17" stop-opacity=".75"/>
        <stop offset="1" stop-color="#1f4a17" stop-opacity="0"/>
      </linearGradient>
    </defs>
    <rect x="0" y="170" width="360" height="260" fill="url(#tint)"/>
    <path d="M0 0 H296 C296 110 250 170 0 190 Z" fill="var(--yellow)"/>
    <path d="M0 0 H282 C280 100 230 160 0 176 Z" fill="var(--white)"/>
    <path d="M0 345 C120 370 230 420 330 420 L330 440 C220 440 100 405 0 380 Z" fill="var(--yellow)"/>
    <path d="M0 380 C100 405 220 440 330 440 L690 440 L690 445 L0 445 Z" fill="var(--white)"/>
    <path d="M21 430 C120 440 230 445 330 445 L669 445 L669 640 Q669 658 651 658 L39 658 Q21 658 21 640 Z" fill="var(--green)"/>
    <path d="M300 452 C380 470 460 470 520 452 L520 462 C460 480 380 480 300 462 Z" fill="var(--yellow)"/>
  </svg>

  <div class="brand">
    <span class="brand-dot"></span>
    <span class="brand-name">Brisk Meadow Builders</span>
  </div>

  <h1 class="tagline">
    <span class="q q-open">&ldquo;</span>A sustainable solution to mobile vending with an iconic farm house architecture<span class="q-close">&rdquo;</span>
  </h1>

  <div class="price-badge">
    <span class="small">Base price</span>
    <span class="big">Starting</span>
    <span class="small">at just</span>
    <span class="price">$65,000</span>
  </div>

  <h2 class="features-title">Base unit features:</h2>

  <ul class="feature-list left">
    <li><svg><use href="#tick"/></svg>Trailer features tandem wheels w/ brakes</li>
    <li><svg><use href="#tick"/></svg>Steel frame construction for fire retardation safety and weight reduction.</li>
    <li><svg><use href="#tick"/></svg>100% Off grid with solar &amp; up to 20 KWH's of lithium battery storage allowing trailer to be used in places not accessible by traditional trailers.</li>
  </ul>
  <div class="divider-v"></div>
  <ul class="feature-list right">
    <li><svg><use href="#tick"/></svg>60 Gallon water supply tank</li>
    <li><svg><use href="#tick"/></svg>70 Gallon waste water tank</li>
    <li><svg><use href="#tick"/></svg>Custom interiors to suit various uses</li>
    <li><svg><use href="#tick"/></svg>Multiple sizes from 12', 16', 20' &amp; 24' long</li>
    <li><svg><use href="#tick"/></svg>Cupboards, cabinets &amp; four stainless steel sinks.</li>
    <li><svg><use href="#tick"/></svg>60 Gas shock serving window</li>
  </ul>

  <div class="unit-photo one" role="img" aria-label="Side view of trailer vending unit with solar panels and serving window"></div>
  <div class="unit-photo two" role="img" aria-label="Front view of tiny farmhouse unit with porch deck"></div>
  <div class="unit-photo three" role="img" aria-label="Three-quarter view of vending unit with awning window and deck"></div>

  <section class="options">
    <h3 class="block-title">Available Options:</h3>
    <ul>
      <li>HVAC-Norvale Mini split</li>
      <li>Cooler/Glass front commercial refrigerator</li>
      <li>Upper loft storagee aera</li>
      <li>Signage and graphics</li>
      <li>Ice machine</li>
      <li>3 foot fold down porch deck</li>
    </ul>
    <p class="note">Other custom options available upon request</p>
  </section>

  <div class="divider-col"></div>

  <section class="use-cases">
    <h3 class="block-title">Use cases:</h3>
    <p><span class="label">Food:</span> Lemonade, coffee, pizza, cookies, doughnuts, farm to table etc.</p>
    <p><span class="label">Retail:</span> Grocery / convenience, clothing, watches, jewelry, flowers, crafts, art.</p>
    <p><span class="label">Fundraisers:</span> Boy/Girl sports, non profits</p>
    <p class="cta">Need a custom branded solution for your business? Let's talk!</p>
  </section>

  <footer class="footer">
    <span><svg viewBox="0 0 14 14"><circle cx="7" cy="7" r="6.2" fill="none" stroke="#1d1d1d" stroke-width="1"/><path d="M4.6 3.8 6 5.4 5.2 6.3C5.7 7.4 6.6 8.3 7.7 8.8L8.6 8 10.2 9.4 9.4 10.4C6.6 10.2 3.8 7.4 3.6 4.6Z" fill="#1d1d1d"/></svg>555-014-2278</span>
    <span><svg viewBox="0 0 14 14"><g fill="none" stroke="#1d1d1d" stroke-width="1"><circle cx="7" cy="7" r="6"/><ellipse cx="7" cy="7" rx="2.6" ry="6"/><path d="M1 7H13M2 4H12M2 10H12"/></g></svg>www.BriskMeadowBuilders.com</span>
    <span><svg viewBox="0 0 14 14"><g fill="none" stroke="#1d1d1d" stroke-width="1"><rect x="1" y="3" width="12" height="8.5"/><path d="M1 3 7 8 13 3"/></g></svg>info@BriskMeadowBuilders.com</span>
  </footer>
</main>
</body>
</html>
```